Website Design

Looking for a less than 30 page website for a new tree service company. Most of the pages would be copies of one another but for each geographical area we service. So, for five areas, we would replicate six services for each area.

Coding

Coded - Design and coding required

```html
<!DOCTYPE html>
<html lang="en">
<head>
<meta charset="utf-8">
<title>Ridgeline Trees</title>
<link rel="stylesheet" href="https://fonts.googleapis.com/css2?family=Krona+One&family=Poppins:wght@400;500;600&family=Marcellus&display=swap">
<style>
:root{
  --gold:#e0a100;
  --forest:#1f3512;
  --forest-deep:#17290c;
  --ink:#111;
  --text:#333;
  --white:#fff;
  --field:#fff;
  --panel:#dde9f3;
}
*{box-sizing:border-box;margin:0;padding:0}
html,body{width:1200px;height:4866px;overflow:hidden}
body{position:relative;font-family:"Poppins",sans-serif;color:var(--text);background:var(--white)}
.abs{position:absolute}
.heading{font-family:"Krona One",sans-serif;color:var(--ink)}
.heading .accent{color:var(--gold)}

/* header */
.topbar{left:0;top:0;width:1200px;height:10px;background:var(--gold);z-index:5}
.nav-bar{left:0;top:10px;width:1200px;height:84px;background:var(--white);z-index:4}
.brand{left:122px;top:10px;width:136px;height:160px;background:var(--white);z-index:6;display:flex;align-items:center;justify-content:center;text-align:center;font-family:"Krona One",sans-serif;font-size:17px;line-height:1.3;color:var(--forest);clip-path:polygon(50% 0,100% 22%,100% 78%,50% 100%,0 78%,0 22%);box-shadow:0 0 0 4px var(--gold)}
.nav{left:410px;top:42px;display:flex;gap:44px;font-family:"Krona One",sans-serif;font-size:13px;color:var(--ink);z-index:6}
.nav .current{color:var(--gold);text-decoration:underline}
.btn{display:flex;align-items:center;height:40px;border-radius:20px;overflow:hidden;font-family:"Marcellus",serif;font-size:15px;letter-spacing:1px;color:var(--white)}
.btn .label{background:var(--gold);height:100%;display:flex;align-items:center;padding:0 22px 0 16px}
.btn .go{width:40px;height:40px;display:flex;align-items:center;justify-content:center;border-radius:0 20px 20px 0}
.btn.dark-go .go{background:var(--forest)}
.btn.light-go .go{background:var(--white)}
.nav-contact{left:938px;top:32px;z-index:6}

/* hero */
.hero{left:0;top:0;width:1200px;height:780px;background:linear-gradient(100deg,#3b4a3a 0%,#6e6a55 35%,#9a7a4f 55%,#4b5b41 80%,#2e3a2b 100%);clip-path:polygon(0 0,100% 0,100% 560px,600px 780px,0 560px)}
.hero-band{left:0;top:560px;width:1200px;height:222px;background:var(--forest);clip-path:polygon(0 50px,600px 222px,1200px 50px,1200px 70px,600px 195px,0 70px)}
.hero-shade{left:0;top:0;width:1200px;height:780px;background:linear-gradient(90deg,rgba(0,0,0,.55),rgba(0,0,0,0) 55%);clip-path:polygon(0 0,100% 0,100% 560px,600px 780px,0 560px)}
.hero-welcome{left:113px;top:278px;font-family:"Krona One",sans-serif;font-size:29px;color:var(--white)}
.hero-title{left:113px;top:318px;font-family:"Krona One",sans-serif;font-size:54px;color:var(--white)}
.hero-btn{left:113px;top:400px}
.play{left:572px;top:258px;width:56px;height:56px}

/* services */
.hex{width:285px;height:320px;clip-path:polygon(50% 0,100% 25%,100% 75%,50% 100%,0 75%,0 25%);display:flex;align-items:center;justify-content:center}
.hex-title{background:var(--gold);font-family:"Krona One",sans-serif;font-size:31px;line-height:1.25;color:var(--white);text-align:center}
.hex-photo{background:linear-gradient(160deg,#5d6b4a,#8a5a35 60%,#3d3a2a)}
.hex-label{width:100%;padding:14px 0;background:rgba(0,0,0,.45);font-family:"Krona One",sans-serif;font-size:18px;color:var(--white);text-align:center}

/* stats */
.stats-photo{left:0;top:1580px;width:662px;height:542px;background:linear-gradient(150deg,#4f6a45,#6d5840 50%,#b49a72)}
.stats-panel{left:662px;top:1580px;width:538px;height:542px;background:linear-gradient(90deg,#2f4a1c,var(--forest-deep))}
.pill{height:72px;border-radius:36px;background:var(--white);font-family:"Krona One",sans-serif;font-size:18px;color:var(--ink);display:flex;align-items:center}
.stat-hex{width:120px;height:134px;background:var(--gold);clip-path:polygon(50% 0,100% 25%,100% 75%,50% 100%,0 75%,0 25%);display:flex;align-items:center;justify-content:center}
.stat-hex-inner{width:104px;height:116px;background:var(--white);clip-path:polygon(50% 0,100% 25%,100% 75%,50% 100%,0 75%,0 25%);display:flex;align-items:center;justify-content:center}

/* about */
.about-photo-a{left:112px;top:2234px;width:404px;height:384px;background:linear-gradient(150deg,#7fa3c8,#c8d6e0 45%,#e56a1c 60%,#3a3a3a)}
.about-photo-b{left:270px;top:2410px;width:330px;height:259px;background:linear-gradient(140deg,#2a2420,#7a4b2a 55%,#c98a4e);border-left:8px solid var(--white);border-top:8px solid var(--white)}
.about-title{left:642px;top:2232px;font-size:32px}
.about-copy{left:644px;top:2292px;width:444px;font-size:13.5px;line-height:26px;letter-spacing:.6px;text-align:justify}
.about-copy p+p{margin-top:10px}
.about-btn{left:748px;top:2566px}

/* map */
.map{left:0;top:2760px;width:1200px;height:506px;background:linear-gradient(180deg,#e6f0f4,#eef1ee 60%,#e9eee9)}
.map-photo{left:138px;top:2831px;width:552px;height:255px;background:linear-gradient(160deg,#6e93bd,#a9b9c7 40%,#b0242c 55%,#5b4a3c)}
.map-card{left:500px;top:3015px;width:190px;height:71px;background:var(--white);border-radius:6px 0 0 0;font-size:14px;line-height:24px;text-align:center;color:var(--ink);display:flex;align-items:center;justify-content:center}
.map-pin{left:704px;top:3003px}

/* posts */
.posts-title{left:0;top:3358px;width:1200px;text-align:center;font-size:32px}
.post{width:312px;top:3434px;height:360px}
.post-img{left:0;top:0;width:312px;height:204px}
.post-cut{left:0;top:176px;width:270px;height:30px;background:var(--white)}
.post-date{left:8px;top:182px;font-size:11px;color:var(--ink)}
.post-head{left:10px;top:218px;padding-left:14px;border-left:4px solid var(--gold);font-size:14px;font-weight:500;color:var(--ink);line-height:24px}
.post-text{left:10px;top:254px;width:260px;font-size:13px;line-height:24px}
.post-more{left:14px;top:332px;font-size:10px;color:var(--ink)}
.arrow{top:3625px}

/* contact */
.contact-photo{left:0;top:3878px;width:1200px;height:567px;background:linear-gradient(110deg,#4a5e3a,#7a8e6a 30%,#9ec3e0 55%,#6aa0cf)}
.contact-panel{left:580px;top:3908px;width:509px;height:492px;background:var(--panel);border-radius:18px;opacity:.97}
.contact-title{left:580px;top:3950px;width:509px;text-align:center;font-size:32px}
.field{height:47px;border-radius:24px;background:var(--field);font-size:11px;color:var(--ink);padding:0 26px;display:flex;align-items:center}
.field.area{height:128px;align-items:flex-start;padding-top:18px;border-radius:22px}
.submit{left:766px;top:4320px}

/* footer */
.footer{left:0;top:4445px;width:1200px;height:421px;background:var(--forest)}
.foot-brand{left:135px;top:4615px;width:170px;text-align:center;font-family:"Krona One",sans-serif;font-size:24px;color:var(--white)}
.foot-col{color:var(--white)}
.foot-col h4{font-family:"Krona One",sans-serif;font-weight:400;font-size:15px;margin-bottom:18px;letter-spacing:1px}
.foot-col li{list-style:none;font-size:12.5px;line-height:29px;letter-spacing:.6px}
.foot-rule{width:1px;background:rgba(255,255,255,.7)}
.socials{display:flex;gap:6px}
.socials span{width:20px;height:20px;border-radius:4px;background:var(--white)}
.contact-item{display:flex;gap:22px;align-items:flex-start;margin-bottom:26px}
.contact-item .badge{width:34px;height:38px;background:var(--white);clip-path:polygon(50% 0,100% 25%,100% 75%,50% 100%,0 75%,0 25%);display:flex;align-items:center;justify-content:center;flex:none}
.contact-item div{font-size:12px;line-height:21px;color:var(--white)}
.foot-line{left:112px;top:4823px;width:976px;height:1px;background:rgba(255,255,255,.5)}
.copyright{left:0;top:4841px;width:1200px;text-align:center;font-size:12px;color:var(--white);letter-spacing:.5px}
</style>
</head>
<body>

<header>
  <div class="abs topbar"></div>
  <div class="abs nav-bar"></div>
  <div class="abs brand">RIDGE<br>LINE<br>TREES</div>
  <nav class="abs nav"><span class="current">Home</span><span>About Us</span><span>Services</span><span>Gallery</span><span>Blog</span></nav>
  <div class="abs btn dark-go nav-contact"><span class="label">Contact</span><span class="go"><svg width="18" height="14" viewBox="0 0 18 14"><path d="M1 7h15M10 1l6 6-6 6" stroke="#fff" stroke-width="2" fill="none"/></svg></span></div>
</header>

<section class="hero-section">
  <div class="abs hero" role="img" aria-label="Arborist in safety gear felling a large tree trunk with a chainsaw"></div>
  <div class="abs hero-shade"></div>
  <div class="abs hero-band"></div>
  <p class="abs hero-welcome">Welcome To</p>
  <h1 class="abs hero-title">RIDGELINE TREES</h1>
  <div class="abs btn light-go hero-btn"><span class="label">Get Started</span><span class="go"><svg width="18" height="14" viewBox="0 0 18 14"><path d="M1 7h15M10 1l6 6-6 6" stroke="#1f3512" stroke-width="2" fill="none"/></svg></span></div>
  <svg class="abs play" viewBox="0 0 56 56"><circle cx="28" cy="28" r="27" fill="#e0a100"/><circle cx="28" cy="28" r="18" fill="none" stroke="#fff" stroke-width="3"/><path d="M24 19l12 9-12 9z" fill="#fff"/></svg>
</section>

<section class="services">
  <div class="abs hex hex-title" style="left:19px;top:892px">Our<br>Services</div>
  <div class="abs hex hex-photo" style="left:312px;top:892px" role="img" aria-label="Worker cutting brush with a chainsaw"><div class="hex-label">Brush Cutting</div></div>
  <div class="abs hex hex-photo" style="left:608px;top:892px" role="img" aria-label="Cleared lot with piles of wood debris"><div class="hex-label">Lot Clearing</div></div>
  <div class="abs hex hex-photo" style="left:907px;top:892px" role="img" aria-label="Arborist grinding a stump"><div class="hex-label">Stump Grinding</div></div>
  <div class="abs hex hex-photo" style="left:160px;top:1158px" role="img" aria-label="Crew removing a tree in a residential garden"><div class="hex-label">Residential Cutting</div></div>
  <div class="abs hex hex-photo" style="left:453px;top:1158px" role="img" aria-label="Crew cutting logs at a commercial site"><div class="hex-label">Commercial Cutting</div></div>
  <div class="abs hex hex-photo" style="left:746px;top:1164px" role="img" aria-label="Worker trimming along a forest edge"><div class="hex-label">Edge Cutting</div></div>
</section>

<section class="stats">
  <div class="abs stats-photo" role="img" aria-label="Arborist in a red helmet cutting into a large trunk"></div>
  <div class="abs stats-panel"></div>
  <div class="abs pill" style="left:600px;top:1640px;width:432px;padding-left:96px">10+ Years Experience</div>
  <div class="abs pill" style="left:640px;top:1757px;width:432px;padding-left:66px">7+Best Climbers</div>
  <div class="abs pill" style="left:600px;top:1882px;width:432px;padding-left:108px">150+ Projects Done</div>
  <div class="abs pill" style="left:640px;top:1999px;width:432px;padding-left:66px">50+ Customers</div>
  <div class="abs stat-hex" style="left:495px;top:1610px"><div class="stat-hex-inner"><svg width="50" height="40" viewBox="0 0 50 40"><circle cx="25" cy="16" r="6" fill="#222"/><path d="M13 36c0-8 6-12 12-12s12 4 12 12z" fill="#222"/><circle cx="38" cy="30" r="7" fill="#e0a100"/><path d="M34 30l3 3 5-5" stroke="#fff" stroke-width="2" fill="none"/></svg></div></div>
  <div class="abs stat-hex" style="left:537px;top:1727px"><div class="stat-hex-inner"><svg width="40" height="50" viewBox="0 0 40 50"><path d="M20 2v46M20 20l-12-8M20 28l12-8" stroke="#222" stroke-width="4" fill="none"/><circle cx="12" cy="30" r="5" fill="#e0a100"/></svg></div></div>
  <div class="abs stat-hex" style="left:495px;top:1852px"><div class="stat-hex-inner"><svg width="46" height="46" viewBox="0 0 46 46"><rect x="26" y="6" width="8" height="36" fill="#222"/><circle cx="14" cy="14" r="5" fill="#222"/><path d="M8 42l4-20h6l4 20" fill="#222"/></svg></div></div>
  <div class="abs stat-hex" style="left:537px;top:1969px"><div class="stat-hex-inner"><svg width="46" height="36" viewBox="0 0 46 36"><circle cx="23" cy="10" r="6" fill="#222"/><circle cx="10" cy="14" r="4.5" fill="#222"/><circle cx="36" cy="14" r="4.5" fill="#222"/><path d="M13 34c0-8 5-12 10-12s10 4 10 12zM2 32c0-6 4-9 8-9s6 2 6 2l-4 7zM44 32c0-6-4-9-8-9s-6 2-6 2l4 7z" fill="#222"/></svg></div></div>
</section>

<section class="about">
  <div class="abs about-photo-a" role="img" aria-label="Arborist in orange shirt and helmet using a chainsaw"></div>
  <div class="abs about-photo-b" role="img" aria-label="Chainsaw cutting through a log with flying sawdust"></div>
  <h2 class="abs heading about-title">About <span class="accent">Us</span></h2>
  <div class="abs about-copy">
    <p>Lorem ipsum dolor sit amet, consectetur adipiscing elit, sed do eiusmod tempor incididunt ut labore et dolore magna aliqua. Ut enim ad minim veniam, quis nostrud exercitation ullamco laboris nisi ut aliquip ex ea commodo consequat.</p>
    <p>Duis aute irure dolor in reprehenderit in voluptate velit esse cillum dolore eu fugiat nulla pariatur. Excepteur sint occaecat cupidatat non proident, sunt in culpa qui officia deserunt mollit anim id est laborum.</p>
  </div>
  <div class="abs btn dark-go about-btn"><span class="label">Get Started</span><span class="go"><svg width="18" height="14" viewBox="0 0 18 14"><path d="M1 7h15M10 1l6 6-6 6" stroke="#fff" stroke-width="2" fill="none"/></svg></span></div>
</section>

<section class="location">
  <div class="abs map" role="img" aria-label="Street map of the neighbourhood around the company yard"></div>
  <div class="abs map-photo" role="img" aria-label="Climber in red jacket working high in a tree"></div>
  <div class="abs map-card">418 Alder Row<br>SE, 49320</div>
  <svg class="abs map-pin" width="28" height="36" viewBox="0 0 28 36"><path d="M14 35C14 35 2 20 2 13a12 12 0 0 1 24 0c0 7-12 22-12 22z" fill="#e5392b"/><circle cx="14" cy="13" r="5" fill="#fff"/></svg>
</section>

<section class="posts">
  <h2 class="abs heading posts-title">Latest <span class="accent">Posts</span></h2>
  <svg class="abs arrow" style="left:34px" width="24" height="16" viewBox="0 0 24 16"><path d="M23 8H2M9 1L2 8l7 7" stroke="#111" stroke-width="2" fill="none"/></svg>
  <svg class="abs arrow" style="left:1132px" width="24" height="16" viewBox="0 0 24 16"><path d="M1 8h21M15 1l7 7-7 7" stroke="#111" stroke-width="2" fill="none"/></svg>

  <article class="abs post" style="left:110px">
    <div class="abs post-img" style="background:linear-gradient(160deg,#4f7fbf,#7a9a5a 50%,#5a4a36)" role="img" aria-label="Climber cutting a tall tree against blue sky"></div>
    <div class="abs post-cut"></div>
    <span class="abs post-date">1.2.24</span>
    <h3 class="abs post-head">Lorem ipsum dolor</h3>
    <p class="abs post-text">Ut enim ad minim veniam quis nostrud exercitation ullamco laboris.</p>
    <span class="abs post-more">Read More...</span>
  </article>
  <article class="abs post" style="left:442px">
    <div class="abs post-img" style="background:linear-gradient(160deg,#3d3a2e,#8a6a48 50%,#2a2620)" role="img" aria-label="Worker sawing a fallen trunk in a forest"></div>
    <div class="abs post-cut"></div>
    <span class="abs post-date">3.2.24</span>
    <h3 class="abs post-head">Lorem ipsum dolor</h3>
    <p class="abs post-text">Ut enim ad minim veniam quis nostrud exercitation ullamco laboris.</p>
    <span class="abs post-more">Read More...</span>
  </article>
  <article class="abs post" style="left:777px">
    <div class="abs post-img" style="background:linear-gradient(160deg,#5a7a40,#8e8a7a 50%,#3b3a36)" role="img" aria-label="Arborist cutting a large trunk into rounds"></div>
    <div class="abs post-cut"></div>
    <span class="abs post-date">5.2.24</span>
    <h3 class="abs post-head">Lorem ipsum dolor</h3>
    <p class="abs post-text">Ut enim ad minim veniam quis nostrud exercitation ullamco laboris.</p>
    <span class="abs post-more">Read More...</span>
  </article>
</section>

<section class="contact">
  <div class="abs contact-photo" role="img" aria-label="Climber roped into a tree cutting a branch"></div>
  <div class="abs contact-panel"></div>
  <h2 class="abs heading contact-title">Contact <span class="accent">Us</span></h2>
  <div class="abs field" style="left:625px;top:4013px;width:205px">Name</div>
  <div class="abs field" style="left:840px;top:4013px;width:205px">Phone</div>
  <div class="abs field" style="left:625px;top:4071px;width:420px">Email</div>
  <div class="abs field" style="left:625px;top:4129px;width:420px;justify-content:space-between">Select Service<svg width="10" height="6" viewBox="0 0 10 6"><path d="M1 1l4 4 4-4" stroke="#111" fill="none"/></svg></div>
  <div class="abs field area" style="left:625px;top:4187px;width:420px">Message</div>
  <div class="abs btn dark-go submit"><span class="label" style="padding:0 26px 0 32px">Submit</span><span class="go"><svg width="18" height="14" viewBox="0 0 18 14"><path d="M1 7h15M10 1l6 6-6 6" stroke="#fff" stroke-width="2" fill="none"/></svg></span></div>
</section>

<footer>
  <div class="abs footer"></div>
  <div class="abs foot-brand">RIDGELINE<br>TREES</div>
  <div class="abs foot-col" style="left:433px;top:4552px">
    <h4>Quick Links</h4>
    <ul><li>Home</li><li>About Us</li><li>Services</li><li>Testimonials</li><li>Gallery</li><li>Blog</li><li>Contact Us</li></ul>
  </div>
  <div class="abs foot-rule" style="left:580px;top:4555px;height:235px"></div>
  <div class="abs foot-col" style="left:645px;top:4552px">
    <h4>Help Links</h4>
    <ul><li>Privacy Policy</li><li>Terms &amp; Condition</li></ul>
    <h4 style="margin-top:30px">Follow Us</h4>
    <div class="socials"><span></span><span></span><span></span><span></span><span></span></div>
  </div>
  <div class="abs foot-rule" style="left:837px;top:4555px;height:235px"></div>
  <div class="abs foot-col" style="left:911px;top:4552px">
    <h4>Contact Details</h4>
    <div class="contact-item"><span class="badge"><svg width="16" height="12" viewBox="0 0 16 12"><rect x="1" y="1" width="14" height="10" fill="none" stroke="#1f3512" stroke-width="1.5"/><path d="M1 1l7 6 7-6" stroke="#1f3512" stroke-width="1.5" fill="none"/></svg></span><div>EMAIL US<br>hello@ridgelinetrees.com</div></div>
    <div class="contact-item"><span class="badge"><svg width="14" height="14" viewBox="0 0 14 14"><path d="M3 1l3 3-2 2c1 2 2 3 4 4l2-2 3 3-2 2C6 13 1 8 1 3z" fill="#1f3512"/></svg></span><div>CALL US<br>+1 555-014-2760</div></div>
    <div class="contact-item"><span class="badge"><svg width="12" height="16" viewBox="0 0 12 16"><path d="M6 15S1 9 1 6a5 5 0 0 1 10 0c0 3-5 9-5 9z" fill="#1f3512"/><circle cx="6" cy="6" r="2" fill="#fff"/></svg></span><div>LOCATION<br>418 Alder Row<br>SE, 49320</div></div>
  </div>
  <div class="abs foot-line"></div>
  <p class="abs copyright">Copyright © 2024 Ridgeline Trees. All rights reserved.</p>
</footer>

</body>
</html>
```